Pantry Circle is an online food market place that connects foodies who make or grow great food with

We would like a 1/2 A4 page size flyer in landscape to promote our new business. We would like to encourage new home foodies to sign up for a membership on our website www.pantrycirclenz.co.nz and we would like customers who are looking for great food in their local community to search our website for their closest home foodie and support a neighbour who is growing or producing creative food locally

Target Market(s)

Creative food lovers

Industry/Entity Type

Landscape

Colors
acd037
f78f20
33b8a4

Requirements
Must have
• Food images and look groovy
• Must be easy to read and stand out on a notice board
• Website address www.pantrycirclenz.co.nz
Nice to have
• We wish to use this flyer in multiple locations and wish to put in different contact details prior to printing

```html
<!DOCTYPE html>
<html lang="en">
<head>
<meta charset="utf-8">
<title>Pantry Circle – Flyer</title>
<link rel="stylesheet" href="https://fonts.googleapis.com/css2?family=PT+Sans:wght@400;700&family=PT+Sans+Narrow:wght@400;700&display=swap">
<style>
  :root {
    --backdrop: #a3a3a3;
    --paper: #ffffff;
    --leaf: #7db843;
    --earth: #4f3220;
    --ink: #3a3a3a;
    --photo-light: #ede6e0;
    --photo-mid: #c9b7a6;
    --photo-deep: #8f7a68;
  }
  * { margin: 0; padding: 0; box-sizing: border-box; }
  html, body { width: 1200px; height: 911px; overflow: hidden; }
  body { background: var(--backdrop); position: relative; font-family: "PT Sans", sans-serif; }

  .flyer {
    position: absolute; left: 116px; top: 114px;
    width: 967px; height: 683px;
    background: var(--paper);
  }

  .brand {
    position: absolute; left: 0; top: 0; width: 504px; height: 316px;
    display: flex; align-items: center; justify-content: center; gap: 14px;
  }
  .brand-dot { width: 26px; height: 26px; border-radius: 50%; background: var(--leaf); }
  .brand-name {
    font-family: "PT Sans Narrow", sans-serif; font-weight: 700;
    font-size: 58px; color: var(--earth); letter-spacing: 0.5px;
  }

  .headline-band {
    position: absolute; left: 0; top: 316px; width: 504px; height: 148px;
    background: var(--earth);
    display: flex; align-items: center; justify-content: center;
  }
  .headline {
    font-family: "PT Sans Narrow", sans-serif; font-weight: 700;
    font-size: 30px; line-height: 39px; color: var(--leaf); text-align: center;
  }

  .benefits {
    position: absolute; left: 60px; top: 492px; width: 390px;
    font-size: 16px; line-height: 21.5px; color: var(--ink); text-align: center;
  }
  .benefits p + p { margin-top: 8px; }

  .side-panel {
    position: absolute; left: 504px; top: 0; width: 463px; height: 683px;
    background: var(--leaf);
  }
  .kitchen-photo {
    position: absolute; left: 34px; top: 0; width: 394px; height: 558px;
    background: linear-gradient(160deg, var(--photo-light) 0%, var(--photo-mid) 55%, var(--photo-deep) 100%);
  }
  .more-info {
    position: absolute; left: 0; top: 580px; width: 463px; text-align: center;
  }
  .more-info-label { font-size: 20px; color: var(--earth); }
  .web-address {
    font-family: "PT Sans Narrow", sans-serif; font-weight: 700;
    font-size: 34px; color: var(--paper); margin-top: 2px;
  }
</style>
</head>
<body>
  <main class="flyer">
    <header class="brand">
      <span class="brand-dot"></span>
      <span class="brand-name">Pantry Circle</span>
    </header>

    <section class="headline-band">
      <h1 class="headline">Be part of our exciting new<br>online food marketplace connecting<br>foodies in your local community</h1>
    </section>

    <section class="benefits">
      <p># As a foodie you can sell your beautiful home produced or home grown produce on our market-place website</p>
      <p># As a food lover you can purchase lovingly grown or prepared food and support your local foodie community while keeping your food miles low</p>
    </section>

    <aside class="side-panel">
      <div class="kitchen-photo" role="img" aria-label="Photo of a smiling home cook in a striped apron tossing a green salad in a glass bowl, surrounded by fresh tomatoes, cucumbers and eggplants in a bright kitchen"></div>
      <div class="more-info">
        <p class="more-info-label">For more information go to:</p>
        <p class="web-address">www.pantrycirclenz.co.nz</p>
      </div>
    </aside>
  </main>
</body>
</html>
```